New Real Estate Listing/ Home for Sale

I need a postcard announcing a home for sale. I want to send 200 to the neighborhood. I have a photo of the home. The postcard will need the company logo. Brisvale Manangement which you should have.
The agents will be Darren Mulvey 301-555-0147 and Susan Ardley at 571-555-0192.
The home has 3 bedrooms and 2 1/2 bathrooms. 3 floors with an open floor plan. Kitchen with granite and stainless steel appliances.
Deck off the kitchen, these are some features to include.
Price is $460,000.
The post card with need the Open Dwelling logo and Homevant logo. The company name needs the office number included 703-555-0168.
The photo is attached, if you can tight up the picture to leave out the other homes on the sides.

Requirements
Must have
• The Company Name is Brisvale Management 703-555-0168. Must have the company logo, must have Open Dwelling logo and Homevant logo and must have Darren Mulvey 301-555-0147 and Susan Ardley 571-555-0192.

```html
<!DOCTYPE html>
<html lang="en">
<head>
<meta charset="utf-8">
<title>Brisvale Management – Home for Sale Postcard</title>
<link rel="stylesheet" href="https://fonts.googleapis.com/css2?family=Source+Sans+3:wght@400;600&display=swap">
<style>
  :root {
    --ink: #111111;
    --brand-red: #ee1c25;
    --rule: #1a1a1a;
    --circle: #bdbdbd;
    --badge-grey: #6d6d6d;
    --paper: #ffffff;
  }
  * { margin: 0; padding: 0; box-sizing: border-box; }
  html, body {
    width: 1200px;
    height: 929px;
    overflow: hidden;
    background: var(--paper);
  }
  .postcard-back {
    position: relative;
    width: 1200px;
    height: 929px;
    background: var(--paper);
    font-family: "Source Sans 3", "Myriad Pro", sans-serif;
    color: var(--ink);
  }

  /* Listing headline */
  .listing {
    position: absolute;
    left: 102px;
    top: 40px;
    width: 790px;
  }
  .listing-title {
    font-size: 32px;
    font-weight: 600;
    line-height: 40px;
  }
  .listing-title .price { color: var(--brand-red); }
  .listing-features {
    list-style: none;
    margin-top: 8px;
    font-size: 20px;
    line-height: 28px;
  }

  /* Company name */
  .brand {
    position: absolute;
    left: 102px;
    top: 268px;
    display: flex;
    align-items: center;
    gap: 16px;
  }
  .brand-square {
    width: 40px;
    height: 40px;
    background: var(--brand-red);
    flex: none;
  }
  .brand-name {
    font-size: 44px;
    font-weight: 400;
    white-space: nowrap;
  }

  /* Office details */
  .office-contact {
    position: absolute;
    left: 102px;
    top: 436px;
    list-style: none;
    font-size: 30px;
    line-height: 59px;
  }

  /* Agents */
  .agents {
    position: absolute;
    left: 102px;
    top: 700px;
    list-style: none;
    font-size: 22px;
    line-height: 34px;
  }
  .agents .agent-name { font-weight: 600; }

  /* Partner marks */
  .partners {
    position: absolute;
    left: 102px;
    top: 800px;
    display: flex;
    gap: 36px;
    font-size: 20px;
  }
  .partner {
    display: flex;
    align-items: center;
    gap: 10px;
    white-space: nowrap;
  }
  .partner-shape {
    width: 24px;
    height: 24px;
    background: var(--badge-grey);
    flex: none;
  }
  .partner-shape.round { border-radius: 50%; }

  /* Mailing side */
  .divider {
    position: absolute;
    left: 558px;
    top: 367px;
    width: 1.5px;
    height: 375px;
    background: var(--rule);
  }
  .address-label {
    position: absolute;
    left: 636px;
    top: 382px;
    font-size: 29px;
    line-height: 36px;
  }
  .address-line {
    position: absolute;
    left: 633px;
    width: 454px;
    height: 1.5px;
    background: var(--rule);
  }
  .address-line.first { top: 481px; }
  .address-line.second { top: 570px; }
  .address-line.third { top: 659px; }
  .postage-area {
    position: absolute;
    left: 917px;
    top: 96px;
    width: 176px;
    height: 176px;
    border: 1.5px solid var(--circle);
    border-radius: 50%;
    display: flex;
    align-items: center;
    justify-content: center;
    text-align: center;
    font-size: 29px;
    line-height: 38px;
  }
  .barcode-label {
    position: absolute;
    left: 558px;
    top: 798px;
    font-size: 29px;
    line-height: 36px;
  }
</style>
</head>
<body>
  <main class="postcard-back">
    <section class="listing">
      <h1 class="listing-title">Home for Sale &middot; <span class="price">$460,000</span></h1>
      <ul class="listing-features">
        <li>3 Bedrooms &middot; 2&frac12; Baths &middot; 3 Floors &middot; Open Floor Plan</li>
        <li>Granite Kitchen &middot; Stainless Steel Appliances &middot; Deck off Kitchen</li>
      </ul>
    </section>

    <div class="brand">
      <span class="brand-square"></span>
      <span class="brand-name">Brisvale Management</span>
    </div>

    <ul class="office-contact">
      <li>4175 Birchwood Lane,</li>
      <li>Suite 210,</li>
      <li>Fairbrook, VA 22199</li>
      <li>703-555-0168</li>
    </ul>

    <ul class="agents">
      <li><span class="agent-name">Darren Mulvey</span> 301-555-0147</li>
      <li><span class="agent-name">Susan Ardley</span> 571-555-0192</li>
    </ul>

    <div class="partners">
      <span class="partner"><span class="partner-shape"></span>Open Dwelling</span>
      <span class="partner"><span class="partner-shape round"></span>Homevant</span>
    </div>

    <div class="divider"></div>

    <p class="address-label">Address Area</p>
    <div class="address-line first"></div>
    <div class="address-line second"></div>
    <div class="address-line third"></div>

    <div class="postage-area">Postage<br>Area</div>

    <p class="barcode-label">Barcode Area</p>
  </main>
</body>
</html>
```